Website re-design for Brookvane LLC website ( has existing website )

Looking to do a complete re-design of Brookvanellc. The existing website is dated and built in wordpress. The new website will not be wordpress. The project folder includes an overview.txt file with details on the project. The file also contains a list of websites that he/she likes which I am sure is very helpful .
Number of Pages Required
1 page

```html
<!DOCTYPE html>
<html lang="en">
<head>
<meta charset="utf-8">
<title>Brookvane LLC</title>
<link href="https://fonts.googleapis.com/css2?family=Roboto:wght@400;500;700&family=Lato:ital,wght@0,400;0,700;1,700&display=swap" rel="stylesheet">
<style>
:root{
  --blue:#0b62b0;
  --blue-deep:#0a4f93;
  --ink:#2b2b2b;
  --muted:#6b6b6b;
  --grey-bg:#f1f1f1;
  --line:#d6d6d6;
  --white:#ffffff;
  --dark:#2d3236;
}
*{box-sizing:border-box;margin:0;padding:0}
html,body{width:1200px;height:5080px;overflow:hidden}
body{position:relative;background:var(--white);font-family:'Lato',sans-serif;color:var(--ink)}
.abs{position:absolute}
h1,h2,h3,h4{font-family:'Roboto',sans-serif;font-weight:500}

/* header */
.site-header{position:absolute;left:0;top:0;width:1200px;height:108px;background:var(--white)}
.brand{position:absolute;left:110px;top:12px;display:flex;align-items:center;gap:10px}
.brand-dot{width:86px;height:86px;border-radius:50%;background:var(--blue)}
.brand-name{font-family:'Roboto',sans-serif;font-size:38px;font-weight:400;color:var(--blue)}
.header-phone{position:absolute;right:112px;top:22px;font-family:'Roboto',sans-serif;font-size:16px;color:var(--ink);display:flex;gap:6px;align-items:center}
.main-nav{position:absolute;right:112px;top:70px;display:flex;gap:22px;font-family:'Roboto',sans-serif;font-size:15px;color:var(--ink)}

/* hero */
.hero{position:absolute;left:0;top:108px;width:1200px;height:670px;overflow:hidden}
.hero-photo{position:absolute;inset:0;background:linear-gradient(160deg,#3d5a2f 0%,#5c7a3a 35%,#2f3f33 70%,#4a5d52 100%)}
.hero-title{position:absolute;left:0;width:1200px;top:235px;text-align:center;font-family:'Roboto',sans-serif;font-weight:700;font-size:56px;line-height:68px;color:var(--white)}
.btn-light{position:absolute;left:497px;top:398px;width:206px;height:64px;border-radius:32px;background:var(--white);color:var(--ink);font-family:'Roboto',sans-serif;font-weight:700;font-size:18px;display:flex;align-items:center;justify-content:center}
.hero-curve{position:absolute;left:0;bottom:0}

/* about */
.about-icon{left:110px;top:812px;width:94px;height:94px;border-radius:50%;background:var(--blue);border:4px solid #c9dcee}
.about-title{left:110px;top:925px;font-size:40px;line-height:56px;color:var(--ink)}
.about-text{left:552px;top:856px;width:510px;font-size:15.5px;line-height:27.5px;color:var(--muted)}
.btn-outline{left:552px;top:1046px;width:145px;height:54px;border:2px solid var(--blue);border-radius:27px;color:var(--blue);font-family:'Roboto',sans-serif;font-weight:500;font-size:16px;display:flex;align-items:center;justify-content:center}

/* services */
.services{left:0;top:1172px;width:1200px;height:913px;background:var(--grey-bg)}
.section-title{position:absolute;left:0;width:1200px;text-align:center;font-size:40px;color:var(--ink)}
.service-icon{position:absolute;width:180px;height:180px;border-radius:50%;background:var(--white);display:flex;align-items:center;justify-content:center;box-shadow:0 2px 10px rgba(0,0,0,.06)}
.service-icon.active{background:var(--blue);border:6px solid var(--white);outline:3px solid var(--blue)}
.service-label{position:absolute;width:200px;text-align:center;font-family:'Roboto',sans-serif;font-size:21px;line-height:31px;color:var(--ink)}
.carousel-arrow{position:absolute;top:218px}
.barge-photo{position:absolute;left:100px;top:443px;width:420px;height:400px;border-radius:50%;border:4px solid var(--blue);background:linear-gradient(180deg,#8fb3d9 0%,#b9c4cc 45%,#8d8d82 70%,#a79b7a 100%)}
.barge-title{position:absolute;left:667px;top:508px;font-size:29px;color:var(--ink)}
.barge-text{position:absolute;left:667px;top:560px;width:420px;font-size:15.5px;line-height:27.5px;color:var(--muted)}

/* employment */
.job-card{position:absolute;top:2236px;width:470px;height:240px;border:2px solid var(--line);border-radius:8px;background:var(--white);overflow:hidden}
.job-photo{position:absolute;left:0;top:0;width:246px;height:240px}
.job-body{position:absolute;left:270px;top:20px;width:185px;font-size:15.5px;line-height:21px;color:var(--muted)}
.job-body h4{font-size:19px;color:var(--ink);margin-bottom:14px}
.job-body p{margin-bottom:10px}
.job-link{font-family:'Roboto',sans-serif;font-weight:500;font-size:15px;color:var(--blue)}

/* testimonials */
.testimonials{left:0;top:2580px;width:1200px;height:516px;background:linear-gradient(90deg,#0a5aa4,#1476c4)}
.testi-photo{left:660px;top:2548px;width:580px;height:580px;border-radius:50%;border:5px solid var(--white);outline:2px solid var(--blue);background:linear-gradient(170deg,#7fb2e0 0%,#6c8f5c 35%,#2e7fa8 60%,#4b8ea0 100%)}
.testi-title{left:110px;top:2640px;font-size:40px;color:var(--white)}
.testi-quote{left:110px;top:2720px;width:530px;font-style:italic;font-weight:700;font-size:24px;line-height:38px;color:var(--white)}
.testi-cite{left:110px;top:2948px;font-size:17px;color:var(--white)}
.testi-nav{left:110px;top:3005px;display:flex;gap:8px}
.testi-nav span{width:20px;height:20px;border-radius:50%;background:var(--white)}

/* gallery */
.gallery-tile{position:absolute;top:3252px;width:284px;height:280px}
.dots{left:576px;top:3575px;display:flex;gap:4px}
.dots span{width:13px;height:13px;border-radius:50%;border:1.5px solid #888}
.dots span.on{background:#888}

/* faqs */
.faqs{left:0;top:3655px;width:1200px;height:780px;background:var(--grey-bg)}
.faq{position:absolute;left:207px;width:786px;height:56px;border:1.5px solid var(--line);border-radius:6px;background:var(--white);font-family:'Roboto',sans-serif;font-size:20px;color:var(--ink);display:flex;align-items:center;padding-left:30px}
.faq.open{background:var(--blue);border-color:var(--blue);color:var(--white)}
.faq .chev{position:absolute;right:14px;top:12px;width:30px;height:30px;border-radius:50%;display:flex;align-items:center;justify-content:center}
.faq.open .chev{background:var(--white)}
.faq-answer{left:240px;top:3863px;width:720px;font-size:15px;line-height:27px;color:var(--muted)}

/* contact */
.contact{left:0;top:4395px;width:1200px;height:685px;background:linear-gradient(180deg,#30363a,#23282b)}
.field{position:absolute;left:110px;width:508px;height:48px;border:1.5px solid #c8c8c8;border-radius:4px;background:rgba(255,255,255,.08);color:var(--white);font-size:17px;padding:12px 16px}
.btn-submit{left:110px;top:4917px;width:116px;height:52px;border-radius:26px;background:var(--white);color:var(--ink);font-family:'Roboto',sans-serif;font-weight:700;font-size:16px;display:flex;align-items:center;justify-content:center}
.contact-brand{left:690px;top:4545px;display:flex;align-items:center;gap:10px}
.contact-brand .brand-dot{width:80px;height:80px;border:3px solid var(--white)}
.contact-line{left:702px;color:var(--white);font-size:18px;line-height:27px;display:flex;gap:10px}
.map-link{left:702px;top:4795px;color:var(--white);font-size:17px;text-decoration:underline}
.copyright{left:110px;top:5030px;color:var(--white);font-size:15px}
.social{left:955px;top:5020px;display:flex;gap:8px}
.social span{width:40px;height:40px;border-radius:50%;border:1.5px solid var(--white)}
</style>
</head>
<body>

<header class="site-header">
  <div class="brand"><span class="brand-dot"></span><span class="brand-name">Brookvane</span></div>
  <div class="header-phone">
    <svg width="14" height="14" viewBox="0 0 24 24"><path fill="#0b62b0" d="M6.6 10.8a15 15 0 006.6 6.6l2.2-2.2a1 1 0 011-.25 11.4 11.4 0 003.6.57 1 1 0 011 1V20a1 1 0 01-1 1A17 17 0 013 4a1 1 0 011-1h3.5a1 1 0 011 1c0 1.25.2 2.45.57 3.57a1 1 0 01-.25 1z"/></svg>
    Call: (555) 214-0187
  </div>
  <nav class="main-nav"><span>About Us</span><span>Services</span><span>Employment</span><span>Testimonials</span><span>Gallery</span><span>FAQs</span><span>Contact Us</span></nav>
</header>

<section class="hero">
  <div class="hero-photo" role="img" aria-label="Divers wading in a lake among lily pads beside a dock"></div>
  <h1 class="hero-title">Keeping Your Shoreline<br>Clean and Pristline</h1>
  <div class="btn-light">FREE ESTIMATE</div>
  <svg class="hero-curve" width="1200" height="670" viewBox="0 0 1200 670">
    <path d="M0 530 Q600 800 1200 530 L1200 670 L0 670Z" fill="#fff"/>
    <path d="M0 530 Q600 800 1200 530" fill="none" stroke="#0b62b0" stroke-width="5"/>
  </svg>
</section>

<section class="about">
  <div class="abs about-icon"></div>
  <h2 class="abs about-title">Aquatic Innovators,<br>at Your Service</h2>
  <p class="abs about-text">Brookvane LLC is a company formed in response to the increasing incidence of invasive species in Minnesota's lakes and water systems. The impact of these fast-growing nuisances, inspired our venture to effectively control unwanted lake weeds. Brookvane, LLC helps provide the enjoyable weed-free lake environment craved by water enthusiasts.</p>
  <div class="abs btn-outline">READ MORE</div>
</section>

<section class="abs services">
  <h2 class="section-title" style="top:58px">Services</h2>
  <svg class="carousel-arrow" style="left:58px" width="20" height="30" viewBox="0 0 20 30"><path d="M15 3L4 15l11 12" fill="none" stroke="#555" stroke-width="2.5"/></svg>
  <svg class="carousel-arrow" style="left:1122px" width="20" height="30" viewBox="0 0 20 30"><path d="M5 3l11 12L5 27" fill="none" stroke="#555" stroke-width="2.5"/></svg>

  <div class="service-icon" style="left:110px;top:143px"><svg width="100" height="70" viewBox="0 0 100 70" fill="none" stroke="#0b62b0" stroke-width="3"><path d="M10 30h40M14 30v25M26 30v25M38 30v25M20 30V14M10 14h20"/><path d="M5 60q8-8 16 0t16 0 16 0 16 0 16 0 10 0"/></svg></div>
  <div class="service-icon" style="left:310px;top:143px"><svg width="90" height="90" viewBox="0 0 90 90" fill="none" stroke="#0b62b0" stroke-width="3"><path d="M10 35L45 12l35 23z M15 35v45M75 35v45M10 38h70"/></svg></div>
  <div class="service-icon active" style="left:504px;top:137px;width:192px;height:192px"><svg width="100" height="80" viewBox="0 0 100 80" fill="none" stroke="#fff" stroke-width="3"><path d="M30 10v22M24 16h12M20 32h60v14H20z M8 46h84l-8 12H16z"/><path d="M10 68q8-6 16 0t16 0 16 0 16 0 16 0"/></svg></div>
  <div class="service-icon" style="left:710px;top:143px"><svg width="90" height="100" viewBox="0 0 90 100" fill="none" stroke="#0b62b0" stroke-width="3"><path d="M40 10v85M54 10v85M10 22h70M40 22L20 40M20 40v18M60 40h20v20H60z M40 50h14M40 70h14"/></svg></div>
  <div class="service-icon" style="left:910px;top:143px"><svg width="90" height="90" viewBox="0 0 90 90" fill="none" stroke="#0b62b0" stroke-width="3"><circle cx="45" cy="45" r="36"/><path d="M20 20l50 50M35 65q-5-20 10-35M50 65q5-18 15-25"/></svg></div>

  <div class="service-label" style="left:100px;top:345px">Dock Install and<br>Removal Services</div>
  <div class="service-label" style="left:300px;top:345px">Canopy<br>Services</div>
  <div class="service-label" style="left:500px;top:345px">Barge Services<br>(Fall 2022)</div>
  <div class="service-label" style="left:700px;top:345px">Dock Lift Services<br>(Fall 2022)</div>
  <div class="service-label" style="left:898px;top:345px">Aquatic Weed<br>Removal</div>

  <div class="barge-photo" role="img" aria-label="Aluminum barge on a trailer beside a building"></div>
  <h3 class="barge-title">Barge Services</h3>
  <p class="barge-text">Nemo enim ipsam voluptatem quia voluptas sit aspera tur aut odit aut fugit, sed quia consequuntur magni dol ores eos qui ratione voluptatem sequi nesciunt. Neque porro quisquam est, qui dolorem ipsum quia dolor sit amet, consectetur, adipisci velit, sed quia non numqu am eius modi tempora incidunt ut.</p>
</section>

<section class="employment">
  <h2 class="section-title" style="top:2143px">Employment</h2>
  <article class="job-card" style="left:110px">
    <div class="job-photo" role="img" aria-label="Diver standing waist-deep in a lake" style="background:linear-gradient(160deg,#4f6f73,#3a5a5a 50%,#6f8b7c)"></div>
    <div class="job-body"><h4>HIRING NOW!</h4><p>Job Title: Diver</p><p>Compensation: Dependent upon qualifications.</p><span class="job-link">MORE DETAILS</span></div>
  </article>
  <article class="job-card" style="left:618px">
    <div class="job-photo" role="img" aria-label="Lake surface covered with floating weeds" style="background:linear-gradient(160deg,#8aa650,#5f86a8 50%,#a7b95a)"></div>
    <div class="job-body"><h4>HIRING NOW!</h4><p>Job Title: Disposal Assistant</p><p>Compensation: Dependent upon qualifications.</p><span class="job-link">MORE DETAILS</span></div>
  </article>
</section>

<section class="abs testimonials"></section>
<div class="abs testi-photo" role="img" aria-label="Dock with boat lift canopies on a clear lake"></div>
<h2 class="abs testi-title">Testimonials</h2>
<p class="abs testi-quote">“Everyone used to jump off the water trampoline and instantly get tangled in lake weeds. We contacted Brookvane and their SCUBA divers have now been solving our problem for the past 4 years!”</p>
<p class="abs testi-cite">– Harlow Pines Association (Lake Ardenwood)</p>
<div class="abs testi-nav"><span></span><span></span></div>

<section class="gallery">
  <h2 class="section-title" style="top:3165px">Gallery</h2>
  <div class="gallery-tile" style="left:13px;background:linear-gradient(180deg,#9cc1de,#5b7f5a 35%,#c9b58e 70%,#a08d6a)" role="img" aria-label="Kayaks and a chair on a sandy beach"></div>
  <div class="gallery-tile" style="left:310px;background:linear-gradient(180deg,#4f86c8,#86aedb 40%,#2f5b86 70%,#8a7b66)" role="img" aria-label="Canopy frame over a boat lift at a dock"></div>
  <div class="gallery-tile" style="left:606px;background:linear-gradient(180deg,#7e8fa8,#e7a35b 45%,#4a4b58 70%,#5c5048)" role="img" aria-label="Sunset over a lake seen from a dock"></div>
  <div class="gallery-tile" style="left:902px;background:linear-gradient(180deg,#b6c4d3,#8ea0b2 40%,#6c7f8d 70%,#9aa8b1)" role="img" aria-label="Calm lake with a dock ladder"></div>
  <div class="abs dots"><span class="on"></span><span></span><span></span></div>
</section>

<section class="abs faqs">
  <h2 class="section-title" style="top:62px">FAQs</h2>
</section>
<div class="faq open" style="top:3785px">How early do lake weeds start to grow?<span class="chev"><svg width="14" height="10" viewBox="0 0 14 10"><path d="M2 8l5-5 5 5" fill="none" stroke="#0b62b0" stroke-width="2"/></svg></span></div>
<p class="abs faq-answer">Curly-leaf pondweed is one of the first plants to grow in early spring (and typically dies off the quickest at the end of the summer). This is heavily dependent on sunlight, how fast the water warms up, and sediment type (sand versus muck).</p>
<div class="faq" style="top:3968px">How fast do lake weeds grow?<span class="chev"><svg width="14" height="10" viewBox="0 0 14 10"><path d="M2 2l5 5 5-5" fill="none" stroke="#777" stroke-width="1.8"/></svg></span></div>
<div class="faq" style="top:4038px">How big of an area can I treat?<span class="chev"><svg width="14" height="10" viewBox="0 0 14 10"><path d="M2 2l5 5 5-5" fill="none" stroke="#777" stroke-width="1.8"/></svg></span></div>
<div class="faq" style="top:4108px">What if the treatment area encroaches your neighbor’s shoreline?<span class="chev"><svg width="14" height="10" viewBox="0 0 14 10"><path d="M2 2l5 5 5-5" fill="none" stroke="#777" stroke-width="1.8"/></svg></span></div>
<div class="faq" style="top:4178px">How long does each treatment last?<span class="chev"><svg width="14" height="10" viewBox="0 0 14 10"><path d="M2 2l5 5 5-5" fill="none" stroke="#777" stroke-width="1.8"/></svg></span></div>
<div class="faq" style="top:4248px">I DO NOT have a natural beach. Can I install one?<span class="chev"><svg width="14" height="10" viewBox="0 0 14 10"><path d="M2 2l5 5 5-5" fill="none" stroke="#777" stroke-width="1.8"/></svg></span></div>

<section class="abs contact" role="img" aria-label="Dimmed photo of a diver at a dock"></section>
<svg class="abs" style="left:0;top:4380px" width="1200" height="140" viewBox="0 0 1200 140">
  <path d="M0 0H1200V115Q600 -60 0 115Z" fill="#f1f1f1"/>
  <path d="M0 115Q600 -60 1200 115" fill="none" stroke="#0b62b0" stroke-width="5"/>
</svg>
<h2 class="section-title" style="top:4448px;color:#fff">Contact Us</h2>
<div class="field" style="top:4548px">Your Name (required)</div>
<div class="field" style="top:4617px">Your Email (required)</div>
<div class="field" style="top:4685px">Subject</div>
<div class="field" style="top:4753px;height:124px">Your Message</div>
<div class="abs btn-submit">SUBMIT</div>
<div class="abs contact-brand"><span class="brand-dot"></span><span class="brand-name" style="color:#fff;font-size:36px">Brookvane</span></div>
<div class="abs contact-line" style="top:4652px"><svg width="16" height="16" viewBox="0 0 24 24" style="margin-top:5px"><path fill="#fff" d="M6.6 10.8a15 15 0 006.6 6.6l2.2-2.2a1 1 0 011-.25 11.4 11.4 0 003.6.57 1 1 0 011 1V20a1 1 0 01-1 1A17 17 0 013 4a1 1 0 011-1h3.5a1 1 0 011 1c0 1.25.2 2.45.57 3.57a1 1 0 01-.25 1z"/></svg>(555) 214-0187</div>
<div class="abs contact-line" style="top:4706px"><svg width="16" height="14" viewBox="0 0 24 20" style="margin-top:6px"><path fill="#fff" d="M2 2h20v16H2z"/><path d="M2 2l10 8 10-8" fill="none" stroke="#2d3236" stroke-width="2"/></svg><span>4180 Birch Lane<br>Westhaven, MN 55000</span></div>
<div class="abs map-link">VIEW MAP</div>
<p class="abs copyright">© 2022 Brookvane, LLC. All rights reserved.</p>
<div class="abs social"><span></span><span></span><span></span></div>

</body>
</html>
```